Poster Design Project

I want word type poster for one place in london that will describe with words.I have attach one mine photo and two relevant text that will describe my city tybe project for the city of london at Fenwold Park.I want something like the eco-typography that I have attach.

Target Market(s)

my audience are adults 20-60

```html
<!DOCTYPE html>
<html lang="en">
<head>
<meta charset="utf-8">
<title>Fenwold Park — London</title>
<link href="https://fonts.googleapis.com/css2?family=Oswald:wght@300;400;500&family=Josefin+Sans:wght@300&display=swap" rel="stylesheet">
<style>
  :root {
    --sky-deep: #3b6cbd;
    --sky-light: #8fb0d6;
    --branches: #6b5443;
    --grass: #6f8f3c;
    --path: #c7a57c;
    --ground-shade: #5e4c3e;
    --text: #ffffff;
    --ornament: rgba(255, 255, 255, 0.55);
  }
  * { margin: 0; padding: 0; box-sizing: border-box; }
  html, body { width: 849px; height: 1200px; overflow: hidden; background: #222; }
  .poster {
    position: relative;
    width: 849px;
    height: 1200px;
    overflow: hidden;
  }
  .poster__scene {
    position: absolute;
    inset: 0;
    background:
      radial-gradient(ellipse at 20% 8%, rgba(255,255,255,0.35), transparent 40%),
      linear-gradient(180deg,
        var(--sky-deep) 0%,
        var(--sky-light) 30%,
        #8c7c6c 48%,
        var(--branches) 62%,
        var(--grass) 70%,
        var(--grass) 74%,
        var(--path) 80%,
        #a68866 90%,
        var(--ground-shade) 100%);
  }
  .story {
    position: absolute;
    left: 268px;
    top: 238px;
    width: 316px;
    color: var(--text);
    font-family: "Oswald", sans-serif;
    font-weight: 400;
    text-transform: uppercase;
    text-align: left;
    text-shadow: 0 1px 3px rgba(0,0,0,0.25);
  }
  .story__title {
    font-size: 56px;
    font-weight: 500;
    letter-spacing: 6px;
    line-height: 58px;
  }
  .story__line {
    display: block;
    font-size: 28.5px;
    line-height: 41.5px;
    white-space: nowrap;
  }
  .story__line--wide { letter-spacing: 4.5px; font-weight: 300; line-height: 36px; }
  .story__line--closing {
    font-size: 20px;
    line-height: 40px;
    text-align: center;
  }
  .city {
    position: absolute;
    left: 0;
    right: 0;
    top: 1108px;
    display: flex;
    align-items: center;
    justify-content: center;
    gap: 18px;
  }
  .city__name {
    font-family: "Josefin Sans", sans-serif;
    font-weight: 300;
    font-size: 72px;
    letter-spacing: 10px;
    color: var(--text);
    line-height: 1;
  }
  .city__flourish {
    width: 62px;
    height: 22px;
    border-radius: 50%;
    background: radial-gradient(ellipse, var(--ornament), transparent 70%);
  }
</style>
</head>
<body>
  <main class="poster">
    <div class="poster__scene" role="img" aria-label="Photograph of a park in winter: bare trees against a blue sky, gulls in flight, green lawn, a path and two people on a bench"></div>

    <section class="story">
      <h1 class="story__title">Fenwold Park</h1>
      <span class="story__line story__line--wide">was created to</span>
      <span class="story__line story__line--wide">satisfy a royal</span>
      <span class="story__line">passion for hunting</span>
      <span class="story__line">but over the years it</span>
      <span class="story__line">became a place where</span>
      <span class="story__line">people have pursued</span>
      <span class="story__line">many other pleasures</span>
      <span class="story__line">Fenwold Park provides a</span>
      <span class="story__line">unique habitat in the</span>
      <span class="story__line">heart of London for</span>
      <span class="story__line">a diverse variety of</span>
      <span class="story__line">species of flora and</span>
      <span class="story__line">and fauna.</span>
      <span class="story__line">the trees shrub beds</span>
      <span class="story__line story__line--closing">and herbaeous plantings</span>
      <span class="story__line story__line--closing">provide rich habitats for</span>
      <span class="story__line story__line--closing">song birds</span>
    </section>

    <footer class="city">
      <span class="city__flourish" role="img" aria-label="Scroll flourish"></span>
      <span class="city__name">LONDON</span>
      <span class="city__flourish" role="img" aria-label="Scroll flourish"></span>
    </footer>
  </main>
</body>
</html>
```